Corporate Design für Holistische Ernährungs- und Gesundheitsberatung
Zielgruppe
Holistische Ernährungs- und Gesundheitsberatung
Es ist an SMARTE Menschen gerichtet, die spüren, dass sie sich gesünder ernähren und auch leben sollten, aber nicht wissen worauf es ankommt und mit welchen Mitteln sie es umsetzen sollen. An Menschen, die vielleicht schon die ersten Zipperlein spüren und erkennen, dass JETZT der Zeitpunkt der Umsetzung gekommen ist und froh um einen EXPERTEN sind, der für verhältnismäßig wenig Geld eine zukunftsweisende Beratung geben kann.
Aufgabenstellung
Es soll stilvoll, schick und modern aussehen. Ein stilisierter (Ess-)Tisch und die Verbindung zu Essen/Lebensmitteln und Gesundheit wären optimal. Bitte keine Assoziation mit Öko (obwohl die alle Recht haben :-))

```html
<!DOCTYPE html>
<html lang="de">
<head>
<meta charset="utf-8">
<title>Tafelwerk Aurel – Geschäftsausstattung</title>
<link href="https://fonts.googleapis.com/css2?family=Montserrat:wght@400;500;600&display=swap" rel="stylesheet">
<style>
  :root {
    --bg: #dcdcdc;
    --paper: #f3f3f1;
    --ink: #2f2f2f;
    --brand: #7b6843;
    --muted: #6d6d6d;
  }
  * { margin: 0; padding: 0; box-sizing: border-box; }
  html, body { width: 1200px; height: 1064px; overflow: hidden; }
  body { background: var(--bg); font-family: "Montserrat", sans-serif; color: var(--ink); position: relative; }

  .letterhead {
    position: absolute; left: 130px; top: 100px; width: 600px; height: 848px;
    background: var(--paper); box-shadow: 0 6px 18px rgba(0,0,0,.18); overflow: hidden;
  }
  .brand { position: absolute; text-align: center; color: var(--brand); }
  .brand-name { font-weight: 500; letter-spacing: .02em; white-space: nowrap; }

  .letterhead .brand { left: 380px; top: 140px; width: 160px; }
  .letterhead .brand-name { font-size: 19px; }

  .sender-line { position: absolute; left: 70px; top: 172px; font-size: 6px; color: var(--muted); }
  .sender-line b { color: var(--brand); font-weight: 500; }

  .recipient { position: absolute; left: 75px; top: 220px; font-size: 10px; line-height: 1.3; font-style: normal; }

  .sender-block { position: absolute; left: 402px; top: 200px; font-size: 9.5px; line-height: 1.3; }
  .sender-block p { margin-bottom: 11px; }
  .contact-list { list-style: none; }
  .contact-list li { display: flex; align-items: center; gap: 5px; }
  .contact-list svg { width: 7px; height: 7px; fill: var(--ink); }
  .date { margin-top: 10px; }

  .letter-body { position: absolute; left: 80px; top: 405px; width: 455px; font-size: 9.6px; line-height: 1.32; }
  .letter-body p { margin-bottom: 12px; }
  .letter-body .closing { margin-top: 18px; margin-bottom: 6px; }
  .signature-space {
    width: 56px; height: 20px;
    background: linear-gradient(90deg, rgba(70,80,160,.18), rgba(70,80,160,.06)); border-radius: 3px;
  }

  .footer-band { position: absolute; left: 0; bottom: 18px; width: 600px; height: 36px; }

  .card {
    position: absolute; left: 818px; width: 260px; height: 150px;
    background: var(--paper); box-shadow: 0 5px 14px rgba(0,0,0,.18);
  }
  .card-front { top: 588px; }
  .card-front .brand { left: 40px; top: 62px; width: 180px; }
  .card-front .brand-name { font-size: 19px; }

  .card-back { top: 800px; }
  .card-back .brand { left: 14px; top: 68px; width: 100px; }
  .card-back .brand-name { font-size: 10px; }
  .card-details { position: absolute; left: 146px; top: 32px; font-size: 5.4px; line-height: 1.3; color: var(--muted); }
  .card-details h2 { font-size: 8px; font-weight: 600; letter-spacing: .06em; color: var(--brand); }
  .card-details .role { margin-bottom: 16px; }
  .card-details .contact-list { margin-top: 8px; }
  .card-details .contact-list li { gap: 4px; align-items: flex-start; }
  .card-details .contact-list svg { width: 5px; height: 5px; margin-top: 1px; fill: var(--muted); }
</style>
</head>
<body>

<svg width="0" height="0" style="position:absolute">
  <defs>
    <symbol id="icon-phone" viewBox="0 0 10 10"><path d="M2 0.5 L3.6 0.5 L4.2 3 L3 3.8 Q4 6 6.2 7 L7 5.8 L9.5 6.4 L9.5 8 Q9.5 9.5 8 9.5 Q1 9 0.5 2 Q0.5 0.5 2 0.5Z"/></symbol>
    <symbol id="icon-mail" viewBox="0 0 10 10"><path d="M0.5 2 H9.5 V8 H0.5Z M1 2.4 L5 5.5 L9 2.4" stroke="#f3f3f1" stroke-width=".8"/></symbol>
    <symbol id="icon-globe" viewBox="0 0 10 10"><circle cx="5" cy="5" r="4.5"/><path d="M0.5 5 H9.5 M5 0.5 V9.5 M5 0.5 Q2 5 5 9.5 M5 0.5 Q8 5 5 9.5" stroke="#f3f3f1" stroke-width=".6" fill="none"/></symbol>
    <symbol id="icon-pin" viewBox="0 0 10 10"><path d="M5 0.5 A3.5 3.5 0 0 1 8.5 4 Q8.5 6 5 9.5 Q1.5 6 1.5 4 A3.5 3.5 0 0 1 5 0.5Z"/><circle cx="5" cy="4" r="1.3" fill="#f3f3f1"/></symbol>
  </defs>
</svg>

<article class="letterhead">
  <div class="brand">
    <div class="brand-name">Tafelwerk Aurel</div>
  </div>

  <div class="sender-line"><b>Tafelwerk Aurel</b> · Lindenhofweg 14 · 70599 Sonnfeld</div>

  <address class="recipient">
    Herr/Frau<br>Martha Mustermann<br>Musterstraße 1<br>12345 Musterstadt
  </address>

  <div class="sender-block">
    <p>Tafelwerk Aurel –<br>Holistische Ernährungs-<br>und Gesundheitsberatung</p>
    <p>Mona Berwald<br>Lindenhofweg 14<br>70599 Sonnfeld</p>
    <ul class="contact-list">
      <li><svg><use href="#icon-phone"/></svg>0170.5550123</li>
      <li><svg><use href="#icon-mail"/></svg>hallo@tafelwerk-aurel.example</li>
      <li><svg><use href="#icon-globe"/></svg>www.tafelwerk-aurel.example</li>
    </ul>
    <div class="date">Sonnfeld, 05.08.2018</div>
  </div>

  <div class="letter-body">
    <p>Sehr geehrte Damen und Herren</p>
    <p>Ditibust laccabo. Harum earum utecto bla cum eumeni bea nat dollaboritia quiatibeaque debis et re conseniminis esed que es enis et de porpori asitaturest autati nusam que num sus.</p>
    <p>Harchitibus es vello velit od qui officiure es si tecte ped moluptae si untori ditistio to omnis sunt aperrum quostio repudae. Ut aut accae labo. Et quaectem cum, et fugit rerum, inis del maximaio omnis acculpa runtem.</p>
    <p>Sequam reptam sitis re evelesti resedit invellant magnam qui idenisque simintibus ad quame rendemperi dem audis milicte sseque con nestist, omnis reheniminim rectotasped quas entis idestem sim fugias exerum am volorerfero odis et re volorae ctatur moloresequo que landictat laboreh endandi volupit fuga.</p>
    <p>Tem ipitation eic tecerita quas dolut utaquiamus maximoles in endam adici dolora dolore pra vene ped ut ut ut alibusam laborem porest, quamus ma dolupta tinctotatia suntibu santem laborep elibus dem es alia porrum reiuri re modit, tem imi, comniae riosae ea eos et resed quam et re, nobis plautat officiur, secullorro velleniscid essi dunt unt videntorume possi untiam doleces tiistia</p>
    <p class="closing">Mit freundlichen Grüßen</p>
    <div class="signature-space" role="img" aria-label="Handschriftliche Unterschrift M. Berwald"></div>
  </div>

  <svg class="footer-band" viewBox="0 0 600 36" aria-hidden="true">
    <path d="M0 8 H250 A50 50 0 0 0 350 8 H600 V36 H0Z" fill="var(--brand)"/>
  </svg>
</article>

<section class="card card-front">
  <div class="brand">
    <div class="brand-name">Tafelwerk Aurel</div>
  </div>
</section>

<section class="card card-back">
  <div class="brand">
    <div class="brand-name">Tafelwerk Aurel</div>
  </div>
  <div class="card-details">
    <h2>MONA BERWALD</h2>
    <div class="role">Holistische Ernährungs-<br>und Gesundheitsberatung</div>
    <ul class="contact-list">
      <li><svg><use href="#icon-pin"/></svg><span>Lindenhofweg 14<br>70599 Sonnfeld</span></li>
    </ul>
    <ul class="contact-list">
      <li><svg><use href="#icon-phone"/></svg>0170.5550123</li>
      <li><svg><use href="#icon-mail"/></svg>hallo@tafelwerk-aurel.example</li>
      <li><svg><use href="#icon-globe"/></svg>www.tafelwerk-aurel.example</li>
    </ul>
  </div>
</section>

</body>
</html>
```